Ward Compass Business Card Design*

We need a business card design for our company Ward Compass. Our company is specialized in providing online consulting services regarding medical institutions, hospitals and doctors. We work with patients worldwide looking to choose between healthcare providers. We have a website you may use as a reference, where we list doctors and clinics worldwide. So we target Medical providers as well as patients worldwide.
Target Market(s)
Medical Providers and patients around the world
Industry/Entity Type
Medical
Contact Information for Business Card
Salma Derkaoui
CEO
+90 612 348 2071
info@wardcompass-example.com
www.wardcompass-example.com
14 Annakhil 3 H.R.B. Rabat, Morocco
Requirements
Must have
- Company logo/name on one full side, personal info and smaller logo and company name on the other side.
Nice to have
- Smart and elegant design

```html
<!DOCTYPE html>
<html lang="en">
<head>
<meta charset="UTF-8">
<title>Ward Compass — Business Card</title>
<link rel="stylesheet" href="https://fonts.googleapis.com/css2?family=Lato:wght@400;700&family=Montserrat:wght@400;700&display=swap">
<style>
  :root {
    --backdrop: #e4e4e6;
    --card-white: #ffffff;
    --brand-blue: #2f7fc4;
    --brand-blue-dark: #2a6fb5;
    --sky-start: #35a8da;
    --sky-end: #2b72b8;
    --ink-light: #ffffff;
    --rule-light: rgba(255, 255, 255, 0.55);
    --shadow: rgba(40, 50, 70, 0.18);
  }
  * { box-sizing: border-box; margin: 0; padding: 0; }
  html, body {
    width: 1200px;
    height: 900px;
    overflow: hidden;
    background: var(--backdrop);
  }
  .sheet {
    width: 1200px;
    height: 900px;
    display: flex;
    flex-direction: column;
    align-items: center;
    justify-content: center;
    gap: 56px;
  }
  .card {
    width: 630px;
    height: 360px;
    border-radius: 26px;
    box-shadow: 0 10px 28px var(--shadow);
    position: relative;
    overflow: hidden;
  }

  /* Front side */
  .card--front {
    background: var(--card-white);
    display: flex;
    flex-direction: column;
    align-items: center;
    justify-content: center;
  }
  .brand {
    display: flex;
    align-items: center;
    gap: 14px;
  }
  .brand__dot {
    width: 38px;
    height: 38px;
    border-radius: 50%;
    background: var(--brand-blue);
  }
  .brand__name {
    font-family: "Montserrat", sans-serif;
    font-weight: 700;
    font-size: 34px;
    letter-spacing: 1px;
    color: var(--brand-blue);
    text-transform: uppercase;
  }
  .website {
    margin-top: 62px;
    font-family: "Lato", sans-serif;
    font-weight: 700;
    font-size: 15px;
    color: var(--brand-blue-dark);
  }

  /* Back side */
  .card--back {
    background: linear-gradient(160deg, var(--sky-start) 0%, var(--sky-end) 100%);
    color: var(--ink-light);
    display: flex;
    flex-direction: column;
    align-items: center;
    padding-top: 54px;
  }
  .back-brand {
    display: flex;
    align-items: center;
    gap: 14px;
  }
  .back-brand__dot {
    width: 44px;
    height: 44px;
    border-radius: 50%;
    background: var(--ink-light);
  }
  .back-brand__name {
    font-family: "Montserrat", sans-serif;
    font-weight: 700;
    font-size: 30px;
    letter-spacing: 1px;
    text-transform: uppercase;
    color: var(--ink-light);
  }
  .rule {
    width: 400px;
    height: 1px;
    background: var(--rule-light);
  }
  .rule--top { margin-top: 42px; }
  .person {
    margin-top: 16px;
    text-align: center;
    font-family: "Lato", sans-serif;
  }
  .person__name {
    font-size: 24px;
    letter-spacing: 0.5px;
    text-transform: uppercase;
  }
  .person__first { font-weight: 700; }
  .person__last { font-weight: 400; }
  .person__role {
    font-size: 16px;
    font-weight: 400;
    margin-top: 2px;
  }
  .contact {
    margin-top: 18px;
    font-family: "Lato", sans-serif;
    font-size: 16px;
    font-weight: 400;
  }
  .contact b { font-weight: 700; }
  .rule--bottom { margin-top: 16px; }
</style>
</head>
<body>
  <main class="sheet">
    <section class="card card--front" aria-label="Card front">
      <div class="brand">
        <span class="brand__dot"></span>
        <span class="brand__name">Ward Compass</span>
      </div>
      <p class="website">www.wardcompass-example.com</p>
    </section>

    <section class="card card--back" aria-label="Card back">
      <div class="back-brand">
        <span class="back-brand__dot"></span>
        <span class="back-brand__name">Ward Compass</span>
      </div>
      <div class="rule rule--top"></div>
      <div class="person">
        <p class="person__name"><span class="person__first">Salma</span> <span class="person__last">Derkaoui</span></p>
        <p class="person__role">CEO</p>
      </div>
      <p class="contact"><b>P:</b> +90 612 348 2071 | <b>E:</b> info@wardcompass-example.com</p>
      <div class="rule rule--bottom"></div>
    </section>
  </main>
</body>
</html>
```